" E uma empresa que trabalha com criaçao de projetos de iluminaçao em geral, tendo ênfase em projetos e Visualizaçao 3D. De acordo com esse video http://www.videoral-exemplo.com/ver?v=Kp7Rb2mTxQa&origem=lstz. "

```html
<!DOCTYPE html>
<html lang="en">
<head>
<meta charset="utf-8">
<title>Moretti Valen – Business Card</title>
<link rel="stylesheet" href="https://fonts.googleapis.com/css2?family=Montserrat:wght@300;600&display=swap">
<style>
  :root {
    --page-bg: #1c1b1a;
    --card-bg: #2b2927;
    --card-edge: #33302d;
    --gold: #b8974f;
    --white: #f4f2ee;
  }
  * { margin: 0; padding: 0; box-sizing: border-box; }
  html, body {
    width: 1200px;
    height: 1200px;
    overflow: hidden;
    background: var(--page-bg);
  }
  .canvas {
    width: 1200px;
    height: 1200px;
    display: flex;
    align-items: center;
    justify-content: center;
  }
  .business-card {
    position: relative;
    width: 1000px;
    height: 572px;
    background: linear-gradient(135deg, var(--card-edge) 0%, var(--card-bg) 55%, #252321 100%);
    box-shadow: 0 30px 60px rgba(0, 0, 0, 0.45);
    overflow: hidden;
  }
  .accent-left {
    position: absolute;
    left: 0;
    top: 150px;
    width: 14px;
    height: 150px;
    background: var(--gold);
  }
  .accent-top {
    position: absolute;
    top: 0;
    right: 120px;
    width: 220px;
    height: 8px;
    background: var(--gold);
  }
  .brand-block {
    position: absolute;
    right: 110px;
    top: 200px;
    text-align: left;
  }
  .brand-row {
    display: flex;
    align-items: center;
    gap: 22px;
  }
  .brand-mark {
    width: 34px;
    height: 34px;
    background: var(--gold);
  }
  .brand-name {
    font-family: "Montserrat", sans-serif;
    font-weight: 300;
    font-size: 56px;
    letter-spacing: 4px;
    color: var(--white);
    text-transform: uppercase;
    line-height: 1;
  }
  .tagline {
    margin-top: 20px;
    margin-left: 56px;
    font-family: "Montserrat", sans-serif;
    font-weight: 600;
    font-size: 26px;
    letter-spacing: 2px;
    color: var(--white);
  }
</style>
</head>
<body>
  <main class="canvas">
    <section class="business-card">
      <div class="accent-left"></div>
      <div class="accent-top"></div>
      <div class="brand-block">
        <div class="brand-row">
          <span class="brand-mark"></span>
          <h1 class="brand-name">Moretti Valen</h1>
        </div>
        <p class="tagline">Lighting solution</p>
      </div>
    </section>
  </main>
</body>
</html>
```